Website redesign for AI startup

Overview
We are looking to have our website https://www.askmorrow.ai/ redesigned to look much more sophisticated and modern. We would like the brand colors to be different and less or no use of the Morrow bird character. We have included some example sites below for designs that we like. Please do not to use the same purple or purple at all on the site as we would like different brand colors and 'too much purple' has been the main comment.

Example sites that we like:
https://www.quellmark.com/
https://pantrix.com/
https://www.dorvanclimate.com/

Requirements
Redesign the following pages from our website, modeling an example site that we like:
-Home page: https://askmorrow.ai
-See an example: https://www.askmorrow.ai/example-page
-Pricing: https://www.askmorrow.ai/pricing
-Product: https://www.askmorrow.ai/how-it-works
-Portal home: https://www.askmorrow.ai/overview (you will need to create an account to view this; the account is free)
New design should be sleek, professional, and modern
The pages should contain the same content that it currently does.
Images on the pages should change to match the new designs and style.
Use different brand colors, these should look professional
The Morrow bird character can be used, but it’s not required. If the bird is used, it should be rarely used and not front-and-center.
Provide both desktop and mobile designs

Target Market(s)

Small business owners

Industry/Entity Type

SaaS tool

Number of Pages Required

5+ page

Requirements
Must have
• modern and sleek design, different brand colors, mobile and web designs

```html
<!DOCTYPE html>
<html lang="en">
<head>
<meta charset="utf-8">
<title>Morrow – Your 24/7 AI Sales Assistant</title>
<link rel="stylesheet" href="https://fonts.googleapis.com/css2?family=Lexend:wght@400;500;600;700;800&family=DM+Sans:wght@400;500;700&display=swap">
<style>
:root{
  --cream:#f9f6ef;
  --cream-2:#fbf3dc;
  --yellow:#fdf08c;
  --yellow-soft:#fff5bf;
  --yellow-btn:#fdf08c;
  --ink:#111111;
  --text:#2d2d2d;
  --muted:#6d6d6d;
  --orange:#f98a12;
  --orange-soft:#fdeedd;
  --dark:#141414;
  --white:#ffffff;
  --grid:rgba(60,50,30,.07);
}
*{box-sizing:border-box;margin:0;padding:0}
html,body{width:1200px;height:4563px;overflow:hidden}
body{background:var(--cream);font-family:"DM Sans",sans-serif;color:var(--text);position:relative}
.abs{position:absolute}
h1,h2,h3,.btn{font-family:"Lexend",sans-serif}
.btn{position:absolute;display:flex;align-items:center;justify-content:center;border-radius:6px;font-weight:600;font-size:14px;color:var(--ink);text-decoration:none}
.btn-yellow{background:var(--yellow-btn)}
.btn-dark{background:var(--ink);color:var(--white)}

.top-grid{left:0;top:0;width:1200px;height:1000px;
  background-image:linear-gradient(var(--grid) 1px,transparent 1px),linear-gradient(90deg,var(--grid) 1px,transparent 1px);
  background-size:44px 44px;
  -webkit-mask-image:linear-gradient(#000 60%,transparent);mask-image:linear-gradient(#000 60%,transparent)}

/* brand name */
.brand{display:flex;align-items:center;gap:12px;font-family:"DM Sans",sans-serif;font-weight:500;color:var(--ink);letter-spacing:.5px}
.brand-dot{border-radius:50%;background:var(--ink)}
.site-header .brand{left:112px;top:22px;font-size:32px}
.site-header .brand-dot{width:18px;height:18px}
.main-nav{left:560px;top:30px;display:flex;gap:33px;font-size:15px;color:var(--ink)}

.hero-title{left:0;width:1200px;top:118px;text-align:center;font-size:54px;font-weight:700;color:var(--ink)}
.hero-sub{left:300px;width:600px;top:200px;text-align:center;font-family:"Lexend",sans-serif;font-weight:600;font-size:20px;line-height:38px;color:var(--ink)}
.hero-video{left:117px;top:440px;width:966px;height:541px;border-radius:24px;
  background:linear-gradient(120deg,#d9dcdc 0%,#b7b8b2 40%,#6d6355 60%,#c9cbc8 100%)}
.play{left:562px;top:674px;width:76px;height:76px;border-radius:50%;background:#fbd81c;display:flex;align-items:center;justify-content:center}

.blob{left:35px;top:1055px}
.calendar{left:128px;top:1159px;width:528px;height:327px;background:var(--white);border-radius:14px;box-shadow:0 10px 30px rgba(0,0,0,.08);padding:34px 28px}
.cal-title{font-family:"Lexend",sans-serif;font-weight:600;font-size:16px;color:var(--ink)}
.cal-month{position:absolute;left:84px;top:64px;width:210px;display:flex;justify-content:space-between;align-items:center;font-size:14px;color:var(--ink)}
.arrow-c{width:30px;height:30px;border-radius:50%;background:var(--orange-soft);display:flex;align-items:center;justify-content:center}
.cal-grid{position:absolute;left:20px;top:118px;display:grid;grid-template-columns:repeat(7,50px);row-gap:8px;text-align:center}
.cal-grid span{height:42px;display:flex;align-items:center;justify-content:center;font-size:13px;color:var(--muted)}
.cal-grid .dow{height:22px;font-size:11px;color:var(--ink)}
.cal-grid .av b{width:40px;height:40px;border-radius:50%;background:var(--orange-soft);color:var(--orange);display:flex;align-items:center;justify-content:center;font-weight:700}
.cal-grid .sel b{background:var(--orange);color:var(--white)}
.times{position:absolute;left:374px;top:118px;display:flex;flex-direction:column;gap:13px}
.times span{width:128px;height:46px;border:1.5px solid #f7c58f;border-radius:6px;display:flex;align-items:center;justify-content:center;color:var(--orange);font-weight:700;font-size:14px}
.feat-h{font-size:35px;font-weight:700;color:var(--ink);line-height:1.35}
.feat-p{font-size:14.5px;line-height:26px;color:var(--text)}

.lead-band{left:0;top:1671px;width:709px;height:342px;background:var(--yellow)}
.lead-box{left:633px;top:1595px;width:450px;height:350px;background:var(--yellow-soft)}
.laptop{left:576px;top:1689px;width:488px;height:305px;border-radius:12px 12px 4px 4px;background:linear-gradient(#2b2b2b 0 4%,#f3f3f5 4% 88%,#9a9a9c 88%)}

.eng-photo{left:112px;top:2084px;width:393px;height:414px;border-radius:4px 4px 22px 4px;background:linear-gradient(135deg,#3a3530 0%,#bda38c 45%,#d9dbe0 100%)}

.testi-band{left:0;top:2600px;width:1200px;height:588px;background:var(--cream-2)}
.testi-h{left:0;width:1200px;top:2650px;text-align:center;font-size:33px;font-weight:700;color:var(--ink)}
.avatar{border-radius:50%;border:3px solid var(--white);box-shadow:0 3px 10px rgba(0,0,0,.12)}
.testi-card{left:268px;top:2776px;width:660px;height:324px;background:var(--white)}
.testi-quote{left:300px;width:600px;top:2858px;text-align:center;font-size:14.5px;line-height:26px;color:var(--muted)}
.testi-rule{left:320px;top:2970px;width:560px;height:1px;background:#e6e6e6}
.testi-name{left:0;width:1200px;top:3010px;text-align:center;font-family:"Lexend",sans-serif;font-size:17px;color:var(--ink)}
.testi-name small{font-family:"DM Sans",sans-serif;font-size:14px;color:var(--text);margin-left:14px}
.qmark{font-family:"Lexend",sans-serif;font-size:120px;color:#ececec;line-height:1}
.nav-dot{width:28px;height:28px;border-radius:50%;display:flex;align-items:center;justify-content:center;font-size:14px}

.card{width:314px;height:403px;background:var(--cream-2);border-radius:4px}
.card-img{width:314px;height:185px;border-radius:4px 4px 0 0}
.card h3{position:absolute;left:24px;top:206px;font-size:21px;font-weight:600;line-height:28px;color:var(--ink)}
.card p{position:absolute;left:22px;top:272px;width:280px;font-size:14px;line-height:28.5px;color:var(--text)}

.cta-band{left:0;top:3795px;width:1200px;height:355px;background:var(--yellow)}
.cta-kicker{left:0;width:1200px;top:3866px;text-align:center;font-family:"Lexend",sans-serif;font-weight:700;font-size:21px;color:var(--ink)}
.cta-h{left:0;width:1200px;top:3905px;text-align:center;font-size:60px;font-weight:700;color:var(--ink)}

.footer{left:0;top:4150px;width:1200px;height:413px;background:var(--dark);color:var(--white)}
.footer .brand{color:var(--white);font-size:44px;left:110px;top:60px}
.footer .brand-dot{width:22px;height:22px;background:var(--white)}
.f-h{font-family:"Lexend",sans-serif;font-weight:600;font-size:18px;color:var(--white)}
.f-list{list-style:none;font-size:14px;line-height:30px;color:#e4e4e4}
.f-contact{font-size:15px;line-height:24px;color:#e4e4e4}
.email-box{left:111px;top:4332px;width:348px;height:42px;border:1px solid #6a6a6a;border-radius:6px;font-size:14px;color:#bdbdbd;padding:11px 16px}
.send{left:417px;top:4336px;width:38px;height:34px;background:var(--yellow);border-radius:5px;display:flex;align-items:center;justify-content:center}
.social{width:28px;height:28px;border-radius:50%;background:#2a2a2a}
.copy{left:0;width:1200px;top:4506px;text-align:center;font-size:14px;color:#e4e4e4}
.copy a{color:var(--yellow)}
</style>
</head>
<body>

<div class="abs top-grid"></div>

<header class="site-header">
  <div class="abs brand"><span class="brand-dot"></span>Morrow</div>
  <nav class="abs main-nav">
    <span>Home</span><span>Product</span><span>Support</span><span>Pricing</span><span>FAQ</span><span>Referral Program</span>
  </nav>
</header>

<section class="hero">
  <h1 class="abs hero-title">Welcome!</h1>
  <p class="abs hero-sub">Save time and get more customers with Morrow: Your 24/7 AI Sales Assistant</p>
  <a class="btn btn-yellow" style="left:419px;top:306px;width:174px;height:61px">See An Example!</a>
  <a class="btn btn-dark" style="left:607px;top:306px;width:175px;height:61px">Create your Morrow</a>
  <div class="abs hero-video" role="img" aria-label="Video still: a sales agent with a headset talking at a desktop computer in a bright office"></div>
  <div class="abs play"><svg width="20" height="20" viewBox="0 0 20 20"><path d="M6 4l10 6-10 6z" fill="#111"/></svg></div>
</section>

<section class="scheduling">
  <svg class="abs blob" width="320" height="480" viewBox="0 0 320 480"><path d="M150 10c90-10 170 40 170 120v200c0 100-100 150-200 140C40 460 0 400 0 330 0 250 60 220 70 150 80 70 90 18 150 10z" fill="#fdf3a8" opacity=".75"/></svg>
  <div class="abs calendar">
    <div class="cal-title">Select a Date &amp; Time</div>
    <div class="cal-month">
      <span class="arrow-c"><svg width="10" height="10" viewBox="0 0 10 10"><path d="M7 1L3 5l4 4" stroke="#f98a12" stroke-width="1.6" fill="none"/></svg></span>
      <span>June 2023</span>
      <span class="arrow-c"><svg width="10" height="10" viewBox="0 0 10 10"><path d="M3 1l4 4-4 4" stroke="#f98a12" stroke-width="1.6" fill="none"/></svg></span>
    </div>
    <div class="cal-grid">
      <span class="dow">SUN</span><span class="dow">MON</span><span class="dow">TUE</span><span class="dow">WED</span><span class="dow">THU</span><span class="dow">FRI</span><span class="dow">SAT</span>
      <span></span><span></span><span></span><span></span><span class="av"><b>1</b></span><span class="av"><b>2</b></span><span>3</span>
      <span>4</span><span class="av"><b>5</b></span><span class="av"><b>6</b></span><span class="av"><b>7</b></span><span class="av"><b>8</b></span><span class="av"><b>9</b></span><span>10</span>
      <span>11</span><span class="av"><b>12</b></span><span class="av sel"><b>13</b></span><span class="av"><b>14</b></span><span class="av"><b>15</b></span><span class="av"><b>16</b></span><span>17</span>
    </div>
    <div class="times"><span>10:00am</span><span>10:30am</span><span>11:00am</span></div>
  </div>
  <h2 class="abs feat-h" style="left:693px;top:1196px">Automated Scheduling</h2>
  <p class="abs feat-p" style="left:693px;top:1258px;width:400px;font-size:13.5px">Morrow books meetings with qualified leads directly on your calendar, streamlining your sales process.</p>
  <a class="btn btn-yellow" style="left:692px;top:1338px;width:202px;height:54px">Book Appointment</a>
</section>

<section class="lead">
  <div class="abs lead-box"></div>
  <div class="abs lead-band"></div>
  <h2 class="abs feat-h" style="left:112px;top:1722px">Lead Qualification<br>&amp; Prioritization</h2>
  <p class="abs feat-p" style="left:112px;top:1826px;width:400px;font-size:13.5px">Morrow captures, engages, and qualifies leads, helping you focus on the most promising opportunities.</p>
  <a class="btn btn-dark" style="left:112px;top:1902px;width:160px;height:55px">Learn More</a>
  <div class="abs laptop" role="img" aria-label="Laptop showing the Morrow account dashboard with a lead's contact details and conversation summary"></div>
</section>

<section class="engagement">
  <div class="abs eng-photo" role="img" aria-label="Photo of two smiling customer support agents wearing headsets, one holding a tablet"></div>
  <h2 class="abs feat-h" style="left:555px;top:2164px;font-size:34px">24/7 Customer Engagement</h2>
  <p class="abs feat-p" style="left:555px;top:2227px;width:470px;font-size:19px;line-height:35px">Morrow interacts with your leads across email, chatbot, phone, and text around the clock.<br>See an example here.a</p>
  <a class="btn btn-yellow" style="left:555px;top:2354px;width:159px;height:55px">Learn More</a>
</section>

<section class="testimonials">
  <div class="abs testi-band"></div>
  <h2 class="abs testi-h">Client Testimonials</h2>
  <div class="abs avatar" role="img" aria-label="Client portrait" style="left:109px;top:2693px;width:48px;height:48px;background:#8a7560"></div>
  <div class="abs avatar" role="img" aria-label="Client portrait" style="left:1041px;top:2693px;width:48px;height:48px;background:#6e5a4c"></div>
  <div class="abs avatar" role="img" aria-label="Client portrait" style="left:208px;top:2808px;width:48px;height:48px;background:#7c6455"></div>
  <div class="abs avatar" role="img" aria-label="Client portrait" style="left:936px;top:2810px;width:50px;height:50px;background:#9a8f86"></div>
  <div class="abs testi-card"></div>
  <div class="abs avatar" role="img" aria-label="Photo of a modern house at dusk" style="left:554px;top:2727px;width:90px;height:90px;background:linear-gradient(#3c5a86,#d8a56a)"></div>
  <p class="abs testi-quote">I love that I can collect information about new potential clients as they interact with my ai assistant. Morrow saves me time and helps me build quality relationships with new clients.</p>
  <div class="abs testi-rule"></div>
  <div class="abs qmark" style="left:400px;top:2985px">&ldquo;</div>
  <div class="abs qmark" style="left:752px;top:2985px">&rdquo;</div>
  <div class="abs testi-name">Dean Harlow<small>Photographer</small></div>
  <svg class="abs" style="left:555px;top:3050px" width="100" height="18" viewBox="0 0 100 18">
    <g fill="#f9a21b">
      <path id="st" d="M8 1l2.2 4.6 5 .6-3.7 3.4 1 5L8 12.2 3.5 14.6l1-5L.8 6.2l5-.6z"/>
      <use href="#st" x="20"/><use href="#st" x="40"/><use href="#st" x="60"/><use href="#st" x="80"/>
    </g>
  </svg>
  <div class="abs nav-dot" style="left:205px;top:2919px;background:#ebe3cf;color:#666">&lsaquo;</div>
  <div class="abs nav-dot" style="left:975px;top:2919px;background:var(--yellow);color:#8a7a10">&rsaquo;</div>
</section>

<section class="features">
  <div class="abs card" style="left:117px;top:3293px">
    <div class="card-img" role="img" aria-label="Photo of a woman browsing clothing in a retail store" style="background:linear-gradient(135deg,#9fb5c9,#e7d9c8 60%,#7d8fa3)"></div>
    <h3>Rapid and Effective<br>AI Training</h3>
    <p>Morrow analyzes your website, allowing Morrow to provide accurate and up-to-date information to your leads.</p>
  </div>
  <div class="abs card" style="left:445px;top:3293px">
    <div class="card-img" role="img" aria-label="Photo of two colleagues talking in a modern office" style="background:linear-gradient(135deg,#7a5a40,#d7c7b2 55%,#a9b2a4)"></div>
    <h3>Customize Your<br>Assistant</h3>
    <p>Change your phone number, email, how Morrow engages with your leads, and much more, turning every interaction into an opportunity.</p>
  </div>
  <div class="abs card" style="left:771px;top:3293px">
    <div class="card-img" role="img" aria-label="Photo of a support agent with a headset working at a laptop" style="background:linear-gradient(135deg,#c7d7e2,#f1f4f6 50%,#4b5663)"></div>
    <h3>Seamless Tool<br>Integration</h3>
    <p>Morrow's streamlined tool integrations effortlessly sync with your existing business tools and platforms, ensuring a smooth and seamless setup.</p>
  </div>
</section>

<section class="cta">
  <div class="abs cta-band"></div>
  <div class="abs cta-kicker">SET UP</div>
  <h2 class="abs cta-h">Your Own Morrow</h2>
  <a class="btn btn-dark" style="left:506px;top:4000px;width:190px;height:54px">Create your Morrow</a>
</section>

<footer class="abs footer">
  <div class="abs brand"><span class="brand-dot"></span>Morrow</div>
  <div class="abs f-h" style="left:111px;top:145px">Subscribe To Our Newsletter</div>

  <div class="abs f-h" style="left:527px;top:80px">Contact Us</div>
  <div class="abs f-contact" style="left:532px;top:118px">
    <svg class="abs" style="left:0;top:4px" width="12" height="15" viewBox="0 0 12 15"><path d="M6 0a5.5 5.5 0 015.5 5.5C11.5 9.5 6 15 6 15S.5 9.5.5 5.5A5.5 5.5 0 016 0z" fill="#fff"/><circle cx="6" cy="5.5" r="2" fill="#141414"/></svg>
    <div style="position:absolute;left:26px;top:0;width:200px">12b Lorem ipsum dolor sit amet, consectetur</div>
    <svg class="abs" style="left:0;top:67px" width="14" height="11" viewBox="0 0 14 11"><rect width="14" height="11" rx="1.5" fill="#fff"/><path d="M1 1.5l6 4.5 6-4.5" stroke="#141414" stroke-width="1.3" fill="none"/></svg>
    <div style="position:absolute;left:26px;top:61px;white-space:nowrap">info@askmorrow.com</div>
    <svg class="abs" style="left:0;top:101px" width="13" height="13" viewBox="0 0 13 13"><path d="M3 0l2 3-1.3 1.6a8 8 0 004.7 4.7L10 8l3 2-1 2.5C6 13 0 7 .5 1z" fill="#fff"/></svg>
    <div style="position:absolute;left:26px;top:95px;white-space:nowrap">+1 888 888 8888</div>
  </div>

  <div class="abs f-h" style="left:757px;top:78px">Quick Link</div>
  <ul class="abs f-list" style="left:759px;top:110px">
    <li>Privacy Policy</li><li>Return Policy</li><li>Payment Policy</li><li>Terms &amp; Conditions</li><li>Shipping Policy</li>
  </ul>
  <div class="abs f-h" style="left:953px;top:78px">Support</div>
  <ul class="abs f-list" style="left:955px;top:110px">
    <li>Contact</li><li>FAQ</li><li>Customer Service</li><li>Order Tracking</li>
  </ul>
  <div class="abs copy" style="top:356px">&copy;Copyrights 2024 <a>Morrow</a> &nbsp;| &nbsp; All Rights Reserved</div>
</footer>

<div class="abs email-box">Enter Your Email</div>
<div class="abs send"><svg width="16" height="16" viewBox="0 0 16 16"><path d="M15 1L1 7l5 2 2 5z" fill="#111"/></svg></div>
<div class="abs social" style="left:117px;top:4395px"></div>
<div class="abs social" style="left:157px;top:4395px"></div>
<div class="abs social" style="left:196px;top:4395px"></div>
<div class="abs social" style="left:235px;top:4395px"></div>

</body>
</html>
```